Riverline Estate Holdings Co.

We need a logo and business card design for a Hong Kong based real estate company, KDT Land. We are want the brand to reflect the owners forward thinking, creative, and trend setting projects, while also reflecting a sense of security and strength. We invest in industrial properties which we convert to co-living or co-working spaces. KDT stands for Greater Bay Area which is the region around southern China including HK, Macau, and 9 other Chinese cities...made up of approx. 68 million people. There are massive infrastructure projects including the bridge to Macau and high-speed rail to SZ and the bridge connecting SZ and Zhongshan.

Target Market(s)

Chinese and western retail investors, as well as institutional investors

Industry/Entity Type

Real Estate Development

Contact Information for Business Card

Owen Tallis
CEO
owen@kdtland-hq.com
M + 852 9416 2057
F + 852 3582 0400
Suite 2207, The Meridale, 41 Larchmont Rd., Central, Hong Kong

Logo Text

kdt land (company name) lifestyle property development (underneath)

Colors

Designer to choose colors to be used in the design.

Requirements
Must have
• Details listed above. One side should include the logo and company name...kdt land in modern, hip styling with "lifestyle property development"
Nice to have
• Could be a Black card, with metallic purple "kdt" and white "land"...but open great design ideas
Should not have
• boring and traditional layout

```html
<!DOCTYPE html>
<html lang="en">
<head>
<meta charset="utf-8">
<title>KDT Land — Identity and Business Card</title>
<link rel="stylesheet" href="https://fonts.googleapis.com/css2?family=Montserrat:wght@400;500;600&display=swap">
<style>
  :root {
    --canvas-bg: #000000;
    --card-bg: #0c0c0d;
    --card-edge: #1d1d1f;
    --brand-purple: #6a3aa8;
    --text-purple: #8a55d6;
    --brand-orange: #c8712f;
    --muted-orange: #b86a33;
    --tagline-grey: #a9a3b3;
  }
  * { box-sizing: border-box; margin: 0; padding: 0; }
  html, body {
    width: 1200px;
    height: 1000px;
    overflow: hidden;
    background: var(--canvas-bg);
    font-family: "Montserrat", sans-serif;
  }
  .canvas {
    position: relative;
    width: 1200px;
    height: 1000px;
  }

  /* Brand lockup: square mark + wordmark + tagline */
  .lockup {
    display: inline-flex;
    flex-direction: column;
    align-items: flex-start;
  }
  .lockup-row {
    display: flex;
    align-items: center;
  }
  .brand-square {
    display: block;
    background: var(--brand-orange);
    flex: none;
  }
  .wordmark {
    font-family: "Montserrat", sans-serif;
    font-weight: 600;
    color: var(--brand-purple);
    letter-spacing: 0.01em;
    line-height: 1;
    white-space: nowrap;
  }
  .tagline {
    font-family: "Montserrat", sans-serif;
    font-weight: 500;
    color: var(--tagline-grey);
    text-transform: uppercase;
    line-height: 1;
    white-space: nowrap;
  }

  .brand-header {
    position: absolute;
    top: 150px;
    left: 0;
    width: 1200px;
    display: flex;
    justify-content: center;
  }
  .brand-header .brand-square { width: 22px; height: 22px; margin-right: 18px; }
  .brand-header .wordmark { font-size: 66px; }
  .brand-header .tagline {
    font-size: 14px;
    letter-spacing: 0.22em;
    margin-top: 16px;
    margin-left: 40px;
  }

  /* Cards */
  .card {
    position: absolute;
    top: 470px;
    width: 540px;
    height: 310px;
    background: var(--card-bg);
    border: 1px solid var(--card-edge);
    box-shadow: 0 20px 40px rgba(0,0,0,0.6);
    overflow: hidden;
  }
  .card-front { left: 45px; }
  .card-back { left: 615px; }

  .card-front .lockup {
    position: absolute;
    left: 48px;
    top: 118px;
  }
  .card-front .brand-square { width: 14px; height: 14px; margin-right: 12px; }
  .card-front .wordmark { font-size: 44px; }
  .card-front .tagline {
    font-size: 9.5px;
    letter-spacing: 0.18em;
    margin-top: 12px;
    margin-left: 26px;
  }

  .card-back .lockup {
    position: absolute;
    left: 30px;
    top: 200px;
  }
  .card-back .brand-square { width: 10px; height: 10px; margin-right: 9px; }
  .card-back .wordmark { font-size: 34px; }
  .card-back .tagline {
    font-size: 7.5px;
    letter-spacing: 0.06em;
    margin-top: 9px;
    margin-left: 19px;
  }

  .divider {
    position: absolute;
    left: 262px;
    width: 3px;
  }
  .divider-top { top: 40px; height: 50px; background: var(--brand-purple); }
  .divider-bottom { top: 104px; height: 180px; background: var(--brand-orange); }

  .contact {
    position: absolute;
    left: 290px;
    top: 40px;
    width: 230px;
    color: var(--text-purple);
    font-size: 11px;
    line-height: 1.55;
  }
  .contact-name {
    font-size: 15px;
    font-weight: 400;
    color: var(--brand-orange);
    letter-spacing: 0.04em;
    text-transform: uppercase;
  }
  .contact-name .given { font-weight: 600; }
  .contact-role {
    font-size: 11px;
    color: var(--muted-orange);
    margin-bottom: 12px;
  }
  .contact-lines { margin-bottom: 14px; }
  .address { font-size: 11px; font-style: normal; }
</style>
</head>
<body>
  <main class="canvas">
    <header class="brand-header">
      <div class="lockup">
        <div class="lockup-row">
          <span class="brand-square"></span>
          <div class="wordmark">KDT LAND</div>
        </div>
        <p class="tagline">Lifestyle Property Development</p>
      </div>
    </header>

    <section class="card card-front" aria-label="Business card front">
      <div class="lockup">
        <div class="lockup-row">
          <span class="brand-square"></span>
          <div class="wordmark">KDT LAND</div>
        </div>
        <p class="tagline">Lifestyle Property Development</p>
      </div>
    </section>

    <section class="card card-back" aria-label="Business card back">
      <div class="lockup">
        <div class="lockup-row">
          <span class="brand-square"></span>
          <div class="wordmark">KDT LAND</div>
        </div>
        <p class="tagline">Lifestyle Property Development</p>
      </div>
      <span class="divider divider-top"></span>
      <span class="divider divider-bottom"></span>
      <div class="contact">
        <p class="contact-name"><span class="given">Owen</span> Tallis</p>
        <p class="contact-role">CEO</p>
        <div class="contact-lines">
          <p>M + 852 9416 2057</p>
          <p>F + 852 3582 0400</p>
          <p>owen@kdtland-hq.com</p>
        </div>
        <address class="address">
          Suite 2207, The Meridale<br>
          41 Larchmont Rd.<br>
          Central, Hong Kong
        </address>
      </div>
    </section>
  </main>
</body>
</html>
```